Etiketten für prämierte BBQ Sauce
tr Grafikstube arbeitet sehr professionell und ist sehr hilfsbereit
Zielgruppe
Wir sind ein junges erfolgreiches BBQ Team und suchen für unsere prämierte Sauce ein Etikett.
Aufgabenstellung
Es ist eine Flasche mit 263 ml, der Umfang ist 18 cm, Höhe für das Etikett 6cm (wobei anhand der Aussparung 5.8 besser wäre). Es muss nicht die ganze Flasche umschliessen
Deckel max. 2.6 im Durchmesser
Folgende Infos müssen ersichtlich sein
Honey Mustard Sauce
263ml
Zutatenliste: Senf, Honig, Ketchup, Gewürze, Zucker, Natürliche Aromen, Essig
Mindesthaltbarkeit
Nach dem Öffnen im Kühlschrank aufbewahren
Like us on Plaudernet
Es wäre schön, wenn sich das Logo im Etikett einbetten würde, muss aber nicht. Jedoch sollte es dann zumindest irgendwo bei den Zutaten oder so ersichtlich sein. Mir persönlich schwebte mal etwas im Stil von Kreide vor so quasi das Logo monochrom mit Kreide. Jedoch ist das auch kein muss es soll aber aufzeigen, dass das Logo auch schwarz/weiss sein darf. Dies ist nur mal eine Idee welche ich hatte aber ich überlasse der Creativen Crowd die Freiheit das Etikett zu gestalten :-)
Bei Fragen einfach melden

```html
<!DOCTYPE html>
<html lang="de">
<head>
<meta charset="utf-8">
<title>Honey Mustard Sauce – Etikett</title>
<link href="https://fonts.googleapis.com/css2?family=IM+Fell+English&family=Lobster&display=swap" rel="stylesheet">
<style>
  :root {
    --canvas: #ffffff;
    --board: #000000;
    --chalk: #f2f2f2;
    --chalk-dim: #bdbdbd;
    --chalk-shade: #2b2b2b;
    --flame-top: #e0582a;
    --flame-bottom: #f2a341;
  }
  * { margin: 0; padding: 0; box-sizing: border-box; }
  html, body { width: 1200px; height: 1200px; overflow: hidden; background: var(--canvas); }
  body { position: relative; font-family: "IM Fell English", Georgia, serif; color: var(--chalk); }

  .label {
    position: absolute; left: 106px; top: 81px;
    width: 983px; height: 315px;
    background: var(--board);
  }
  .label-frame { position: absolute; inset: 0; }

  .social {
    position: absolute; left: 104px; top: 44px; width: 110px;
    display: flex; flex-direction: column; align-items: center; gap: 3px;
    font-size: 13px;
  }
  .social-mark { width: 28px; height: 28px; border: 2px solid var(--chalk); }

  .care-info {
    position: absolute; left: 39px; top: 108px; width: 240px;
    text-align: center; font-size: 18px; line-height: 29px;
  }
  .best-before-field {
    position: absolute; left: 57px; top: 234px; width: 206px; height: 30px;
    background: linear-gradient(180deg, #f4f4f4, #d6d6d6);
    border-radius: 3px;
  }

  .product-title {
    position: absolute; left: 365px; top: 14px; width: 260px;
    font-family: "Lobster", "Brush Script MT", cursive;
    font-weight: 400; font-size: 60px; line-height: 58px;
    color: var(--chalk);
    text-align: center;
    transform: rotate(-9deg);
    transform-origin: center;
  }
  .product-title span { display: block; }
  .product-title .line-honey { padding-left: 30px; }
  .product-title .line-sauce { padding-left: 20px; }

  .brand {
    position: absolute; left: 428px; top: 212px; width: 120px;
    display: flex; flex-direction: column; align-items: center; gap: 6px;
    font-size: 16px;
  }
  .brand-dot {
    width: 46px; height: 46px; border-radius: 50%;
    background: linear-gradient(180deg, var(--flame-top), var(--flame-bottom));
  }
  .volume { position: absolute; left: 547px; top: 208px; font-size: 26px; }

  .ingredient-sketch {
    position: absolute; left: 697px; top: 50px; width: 209px; height: 100px;
    background: radial-gradient(ellipse at center, #4a4a4a 0%, #1c1c1c 70%, var(--board) 100%);
    border-radius: 8px;
  }
  .ingredients {
    position: absolute; left: 680px; top: 156px; width: 240px;
    text-align: center; font-size: 19px; line-height: 29px;
  }

  .cap-sticker {
    position: absolute; left: 728px; top: 636px; width: 150px; height: 150px;
    border-radius: 50%; background: var(--board);
    border: 6px solid #3a3a3a;
    display: flex; flex-direction: column; align-items: center; justify-content: center; gap: 8px;
    font-size: 16px;
  }
  .cap-sticker .brand-dot { width: 40px; height: 40px; }
</style>
</head>
<body>
  <section class="label" aria-label="Flaschenetikett Honey Mustard Sauce">
    <svg class="label-frame" width="983" height="315" viewBox="0 0 983 315" aria-hidden="true">
      <g fill="none" stroke="var(--chalk-dim)">
        <rect x="16" y="22" width="953" height="272" stroke-width="2.5"/>
        <rect x="26" y="32" width="933" height="252" stroke-width="1.2"/>
      </g>
      <g fill="var(--chalk-dim)">
        <circle cx="16" cy="22" r="6"/>
        <circle cx="969" cy="22" r="6"/>
        <circle cx="16" cy="294" r="6"/>
        <circle cx="969" cy="294" r="6"/>
      </g>
    </svg>

    <div class="social">
      <span class="social-mark"></span>
      <span class="social-name">Plaudernet</span>
    </div>

    <p class="care-info">
      Like us on Plaudernet<br>
      Nach dem Öffnen im<br>
      Kühlschrank aufbewahren<br>
      Mindesthaltbarkeit
    </p>
    <div class="best-before-field" aria-label="Feld für Mindesthaltbarkeitsdatum"></div>

    <h1 class="product-title">
      <span class="line-honey">Honey</span>
      <span class="line-mustard">Mustard</span>
      <span class="line-sauce">Sauce</span>
    </h1>

    <div class="brand">
      <span class="brand-dot"></span>
      <span class="brand-name">Glutwerk BBQ</span>
    </div>
    <p class="volume">263 ml</p>

    <div class="ingredient-sketch" role="img" aria-label="Kreidezeichnung: Honiglöffel und Schaufel mit Senfkörnern"></div>
    <p class="ingredients">
      Zutatenliste:<br>
      Senf, Honig, Ketchup,<br>
      Gewürze, Zucker,<br>
      Natürliche Aromen, Essig
    </p>
  </section>

  <section class="cap-sticker" aria-label="Deckeletikett">
    <span class="brand-dot"></span>
    <span class="brand-name">Glutwerk BBQ</span>
  </section>
</body>
</html>
```